Design a Site That Says: ‘This is the Next Big Thing in Defense Tech

We are redesigning the Torvik Skyworks website to deliver a bold, high-impact digital experience that convinces on-the-fence investors this is the moment to get involved. The site must feel fast-moving, technology-forward, and unlike anything coming out of traditional aerospace — no more beige PDFs or outdated defense branding. It should reflect the precision, autonomy, and scale of our product without revealing the proprietary details. Through sleek, modern visuals, sharp messaging, and subtle cues of aerospace innovation — airport runways, carbon fiber textures, night imagery, and mission-ready tone — we want to guide the audience toward one powerful conclusion: Torvik Skyworks is building the future of autonomous defense aviation, and the time to invest is now.
✈️ What Is Torvik Skyworks?
Torvik Skyworks is a next-generation autonomous aerial system built for the future of defense. Where legacy drones were designed for one-off missions and slow production pipelines, Torvik is built from the ground up for speed, scalability, and autonomy. Its sleek, tailless design reflects not just a new aircraft, but a new philosophy: one where performance, flexibility, and manufacturing efficiency converge.

This is not another iteration — it’s a complete rethink of how unmanned systems should be built, deployed, and scaled.

🧩 Competitive Discriminators
1. Production-First Philosophy
Most aircraft are built like custom machines. Torvik is different — it’s engineered for rapid production using cutting-edge methods adapted from high-rate industries. This isn’t just about speed — it’s about being able to respond to demand in real time.

2. Autonomy at the Core
Torvik doesn’t rely on ground crews or remote pilots. It’s built for full autonomy — to operate as a single asset or as part of a larger, coordinated swarm without micromanagement.

3. Modularity Without Compromise
One airframe. Many missions. With a modular internal architecture, Torvik can be adapted to a wide range of operational roles without altering its core structure — or its production rhythm.

4. Clean Configuration, Internal Systems
Everything is housed inside — systems, sensors, payloads — resulting in a streamlined platform that looks and performs differently from the start.

5. Distinct Visual Signature
From its tailless form to its smooth composite surfaces, Torvik Skyworks looks like the future — because it is. It’s what happens when aerospace engineers design without compromise.

👀 What Will Stand Out — Even to a Casual Observer
It doesn’t look like any drone they’ve seen before.
No tail, no hardpoints, no draggy silhouettes — just smooth geometry and silent confidence.

It feels like it belongs to the next generation.
While legacy platforms show their age, Torvik shows what’s next. It looks engineered, not assembled.

It invites imagination.
Observers can’t help but wonder: What’s inside? What can it do? How is it built so differently?

It feels like a system, not just an aircraft.
From design to production to deployment, everything about Torvik is intentional — and scalable.

```html
<!DOCTYPE html>
<html lang="en">
<head>
<meta charset="UTF-8">
<title>Torvik Skyworks — The Future of Defense Aviation</title>
<link href="https://fonts.googleapis.com/css2?family=Michroma&family=Montserrat:wght@400;500;600;700&display=swap" rel="stylesheet">
<style>
:root{
  --blue:#0b6cbf;
  --blue-deep:#0a5ea8;
  --ink:#111418;
  --muted:#5d6670;
  --pale:#dfe9f2;
  --white:#ffffff;
  --black:#050505;
}
*{box-sizing:border-box;margin:0;padding:0}
html,body{width:1200px;height:4098px;overflow:hidden}
body{position:relative;font-family:'Montserrat',sans-serif;color:var(--ink);background:var(--white)}
.abs{position:absolute}
.display{font-family:'Michroma',sans-serif;text-transform:uppercase;letter-spacing:0}

/* header */
.brand{font-family:'Michroma',sans-serif;font-size:18px;color:var(--ink);letter-spacing:1px;display:flex;align-items:center;gap:12px;white-space:nowrap}
.brand-dot{width:36px;height:36px;border-radius:50%;background:var(--blue);flex:none}
.site-header .brand{left:95px;top:16px}
.main-nav{left:496px;top:26px;display:flex;font-size:13px;font-weight:700;text-transform:uppercase;white-space:nowrap}
.main-nav a{color:var(--ink);text-decoration:none}
.main-nav a.active{color:var(--blue)}
.main-nav .sep{margin:0 18px}
.nav-search{left:1074px;top:27px}

/* hero */
.hero-bg{left:0;top:0;width:1200px;height:1082px;background:
  radial-gradient(ellipse 420px 300px at 50% 62%,rgba(120,140,165,.35) 0%,rgba(120,140,165,0) 100%),
  radial-gradient(ellipse at 50% 40%,#eef3f8 0%,#d3e0ec 45%,#a9c0d6 80%,#8eaac6 100%)}
.hero-title{left:0;top:128px;width:1200px;text-align:center;font-size:47px;line-height:62px;color:var(--ink)}
.hero-title .accent{color:var(--blue)}
.hero-sub{left:0;top:266px;width:1200px;text-align:center;font-size:19px;font-weight:500;text-transform:uppercase;color:var(--ink)}
.btn{display:flex;align-items:center;justify-content:center;gap:14px;background:var(--blue);color:var(--white);font-weight:700;font-size:15px;text-transform:uppercase;clip-path:polygon(4% 0,96% 0,100% 50%,96% 100%,4% 100%,0 50%)}
.hero-btn{left:439px;top:326px;width:321px;height:49px}
.hero-curve{left:0;top:970px}

/* about */
.about-art{left:118px;top:1149px;width:448px;height:448px;border-radius:50%;background:radial-gradient(circle at 50% 45%,#1b6d9c 0%,#0e3658 45%,#0a1a33 100%);box-shadow:0 20px 40px rgba(0,0,0,.18)}
.section-title{font-size:36px;color:var(--ink)}
.about-title{left:665px;top:1150px}
.rule{height:3px;background:var(--blue)}
.about-rule{left:665px;top:1203px;width:66px}
.about-copy{left:665px;top:1222px;width:440px;font-size:13.5px;line-height:25.5px;color:var(--muted)}
.about-copy p+p{margin-top:18px}
.about-btn{left:665px;top:1503px;width:230px;height:49px}
.about-wave{left:0;top:1380px;width:1200px;height:360px;background:linear-gradient(180deg,rgba(255,255,255,0) 0%,rgba(223,233,242,.6) 100%)}

/* discriminators */
.disc-bg{left:0;top:1690px}
.disc-title{left:0;top:1782px;width:1200px;text-align:center}
.disc-art{left:346px;top:2081px;width:508px;height:400px;border-radius:50%;background:radial-gradient(ellipse at 45% 35%,#f4d9b4 0%,#c9d3df 35%,#8ea6be 70%,#5d7890 100%)}
.node{width:98px;height:98px;border-radius:50%;display:flex;align-items:center;justify-content:center;box-shadow:0 6px 14px rgba(0,0,0,.2)}
.node.blue{background:var(--blue);border:4px solid var(--white);outline:2px solid var(--blue)}
.node.dark{background:var(--black);border:4px solid var(--white);outline:2px solid var(--black)}
.node-label{font-size:15px;font-weight:700;text-transform:uppercase;line-height:25px}
.node-label.blue{color:var(--blue)}
.disc-note{left:300px;top:2534px;width:600px;text-align:center;font-size:14px;line-height:26px;color:var(--muted)}

/* stand out */
.stand-bg{left:0;top:2660px}
.stand-title{left:0;top:2760px;width:1200px;text-align:center;font-size:36px;line-height:46px;color:var(--white)}
.stand-rule{left:562px;top:2866px;width:76px;background:var(--white)}
.card{width:696px;height:140px;border:1.5px solid rgba(255,255,255,.55);border-radius:4px;display:flex;align-items:center;color:var(--white)}
.card-icon{width:105px;height:100%;display:flex;align-items:center;justify-content:center;border-right:1.5px solid rgba(255,255,255,.55);flex:none}
.card-body{padding:0 38px}
.card-title{font-size:15px;font-weight:700;text-transform:uppercase;margin-bottom:10px}
.card-text{font-size:14px;line-height:26px}

/* footer */
.site-footer{left:0;top:3594px;width:1200px;height:504px;background:var(--black);color:var(--white)}
.footer-brand{left:0;top:86px;width:1200px;justify-content:center;color:var(--white);position:absolute;font-size:26px}
.footer-brand .brand-dot{width:44px;height:44px}
.footer-nav{left:0;top:186px;width:1200px;justify-content:center;position:absolute;display:flex;font-size:13px;font-weight:700;text-transform:uppercase}
.footer-nav .sep{margin:0 18px}
.contact{position:absolute;display:flex;gap:18px;top:244px}
.contact-icon{width:42px;height:42px;border-radius:50%;background:var(--white);display:flex;align-items:center;justify-content:center;flex:none}
.contact h4{font-size:14px;font-weight:700;text-transform:uppercase;margin-top:2px;margin-bottom:6px}
.contact p{font-size:13px;line-height:22px}
.footer-line{position:absolute;left:180px;top:378px;width:839px;height:1px;background:rgba(255,255,255,.45)}
.social{position:absolute;top:359px;left:535px;display:flex;gap:8px}
.social span{width:38px;height:38px;border-radius:50%;background:var(--white);display:block}
.copyright{position:absolute;left:0;top:434px;width:1200px;text-align:center;font-size:13px}
</style>
</head>
<body>

<section class="hero">
  <div class="abs hero-bg" role="img" aria-label="Silver fighter jet flying toward the viewer above a sky of soft white clouds with a faint network of connected points"></div>
  <svg class="abs hero-curve" width="1200" height="120" viewBox="0 0 1200 120">
    <path d="M0 120 L0 104 Q300 60 540 40 L600 10 L660 40 Q900 60 1200 104 L1200 120 Z" fill="#0b6cbf"/>
    <path d="M0 120 L0 114 Q300 74 548 54 L600 30 L652 54 Q900 74 1200 114 L1200 120 Z" fill="#ffffff"/>
  </svg>
  <header class="site-header">
    <div class="abs brand"><span class="brand-dot"></span>TORVIK SKYWORKS</div>
    <nav class="abs main-nav">
      <a class="active" href="#">Home</a><span class="sep">|</span>
      <a href="#">About Us</a><span class="sep">|</span>
      <a href="#">Why Torvik</a><span class="sep">|</span>
      <a href="#">Investor Info</a><span class="sep">|</span>
      <a href="#">Contact Us</a>
    </nav>
    <svg class="abs nav-search" width="14" height="14" viewBox="0 0 14 14"><circle cx="6" cy="6" r="4.5" fill="none" stroke="#111418" stroke-width="2"/><line x1="9.5" y1="9.5" x2="13" y2="13" stroke="#111418" stroke-width="2"/></svg>
  </header>
  <h1 class="abs display hero-title">The Future of Defense<br>Aviation is <span class="accent">Autonomous</span></h1>
  <p class="abs hero-sub">Invest in the next generation with Torvik Skyworks</p>
  <a class="abs btn hero-btn">Invest in the future
    <svg width="22" height="14" viewBox="0 0 22 14"><path d="M2 7h16M12 1l6 6-6 6" fill="none" stroke="#fff" stroke-width="2"/></svg></a>
</section>

<section class="about">
  <div class="abs about-wave"></div>
  <div class="abs about-art" role="img" aria-label="Glowing blue wireframe stealth jet on a night runway"></div>
  <h2 class="abs display section-title about-title">About Us</h2>
  <div class="abs rule about-rule"></div>
  <div class="abs about-copy">
    <p>Torvik Skyworks is a next-generation autonomous aerial system built for the future of defense. Where legacy drones were designed for one-off missions and slow production pipelines, Torvik is built from the ground up for speed, scalability, and autonomy. Its sleek, tailless design reflects not just a new aircraft, but a new philosophy: one where performance, flexibility, and manufacturing efficiency converge.</p>
    <p>This is not another iteration – it’s a complete rethink of how unmanned systems should be built, deployed, and scaled.</p>
  </div>
  <a class="abs btn about-btn">View More
    <svg width="22" height="14" viewBox="0 0 22 14"><path d="M2 7h16M12 1l6 6-6 6" fill="none" stroke="#fff" stroke-width="2"/></svg></a>
</section>

<section class="discriminators">
  <svg class="abs disc-bg" width="1200" height="1000" viewBox="0 0 1200 1000">
    <path d="M0 40 Q300 -10 600 30 Q900 70 1200 20 L1200 1000 L0 1000 Z" fill="#dfe9f2"/>
    <path d="M270 560 Q330 420 425 357 M425 357 Q520 305 592 290 M592 290 Q720 300 804 347 M804 347 Q900 410 975 484" fill="none" stroke="#0b6cbf" stroke-width="2" stroke-dasharray="2 5"/>
  </svg>
  <h2 class="abs display section-title disc-title">Competitive Discriminators</h2>
  <div class="abs disc-art" role="img" aria-label="Futuristic tailless white aircraft flying above a sunlit sea of clouds"></div>

  <div class="abs node-label blue" style="left:442px;top:1867px;width:316px;text-align:center">Modularity without<br>compromise</div>
  <div class="abs node blue" style="left:543px;top:1926px">
    <svg width="54" height="54" viewBox="0 0 54 54" fill="none" stroke="#fff" stroke-width="2"><rect x="17" y="17" width="20" height="20" rx="3"/><circle cx="27" cy="27" r="5"/><path d="M27 4v13M27 37v13M4 27h13M37 27h13"/><circle cx="27" cy="4" r="2"/><circle cx="27" cy="50" r="2"/><circle cx="4" cy="27" r="2"/><circle cx="50" cy="27" r="2"/></svg>
  </div>

  <div class="abs node-label" style="left:100px;top:2016px;width:205px;text-align:right">Autonomy<br>at the core</div>
  <div class="abs node dark" style="left:330px;top:1998px">
    <svg width="54" height="54" viewBox="0 0 54 54" fill="none" stroke="#fff" stroke-width="2"><circle cx="21" cy="21" r="10"/><circle cx="21" cy="21" r="4"/><circle cx="36" cy="36" r="9"/><circle cx="36" cy="36" r="3"/><path d="M21 7v4M21 31v4M7 21h4M31 21h4M36 23v4M36 45v4M23 36h4M45 36h4"/></svg>
  </div>

  <div class="abs node-label" style="left:869px;top:1994px;width:260px">Clean configuration<br>internal systems</div>
  <div class="abs node dark" style="left:755px;top:1988px">
    <svg width="58" height="58" viewBox="0 0 58 58" fill="none" stroke="#fff" stroke-width="2"><circle cx="22" cy="22" r="12"/><circle cx="22" cy="22" r="5"/><circle cx="39" cy="38" r="11"/><circle cx="39" cy="38" r="4"/><path d="M22 6v4M22 34v4M6 22h4M34 22h4M39 23v4M39 49v4M24 38h4M50 38h4"/></svg>
  </div>

  <div class="abs node-label" style="left:90px;top:2245px;width:203px;text-align:right">Production-first<br>philosophy</div>
  <div class="abs node blue" style="left:177px;top:2135px">
    <svg width="54" height="54" viewBox="0 0 54 54" fill="none" stroke="#fff" stroke-width="2"><circle cx="27" cy="27" r="17"/><circle cx="27" cy="27" r="10"/><path d="M22 27l4 4 7-8"/><path d="M27 5v5M27 44v5M5 27h5M44 27h5M11 11l4 4M39 39l4 4M43 11l-4 4M11 43l4-4"/></svg>
  </div>

  <div class="abs node-label" style="left:934px;top:2245px;width:220px">Distinct visual<br>signature</div>
  <div class="abs node blue" style="left:925px;top:2125px">
    <svg width="54" height="54" viewBox="0 0 54 54" fill="none" stroke="#fff" stroke-width="2"><path d="M34 6l8 8-18 22-9 2 2-9z"/><path d="M8 44c6-4 8 2 12-1s6-3 10 0"/></svg>
  </div>

  <p class="abs disc-note">One airframe. Many missions. With a modular internal architecture, Torvik can be adapted to a wide range of operational roles without altering its core structure — or its production rhythm.</p>
</section>

<section class="stand-out">
  <svg class="abs stand-bg" width="1200" height="934" viewBox="0 0 1200 934">
    <defs><linearGradient id="standGrad" x1="0" y1="0" x2="0" y2="1"><stop offset="0" stop-color="#0b6cbf"/><stop offset="1" stop-color="#0a5ea8"/></linearGradient></defs>
    <path d="M0 46 Q600 -20 1200 46 L1200 934 L0 934 Z" fill="url(#standGrad)"/>
  </svg>
  <h2 class="abs display stand-title">What will stand out<br>even to a casual observer</h2>
  <div class="abs rule stand-rule"></div>

  <article class="abs card" style="left:216px;top:2908px">
    <div class="card-icon"><svg width="70" height="70" viewBox="0 0 70 70" fill="none" stroke="#fff" stroke-width="2"><circle cx="16" cy="16" r="9"/><circle cx="54" cy="16" r="9"/><circle cx="16" cy="54" r="9"/><circle cx="54" cy="54" r="9"/><rect x="28" y="28" width="14" height="14" rx="3"/><path d="M22 22l6 6M48 22l-6 6M22 48l6-6M48 48l-6-6"/></svg></div>
    <div class="card-body"><h3 class="card-title">It doesn’t look like any drone they’ve seen before</h3><p class="card-text">No tail, no hardpoints, no draggy silhouettes — just smooth geometry and silent confidence</p></div>
  </article>

  <article class="abs card" style="left:302px;top:3064px">
    <div class="card-icon"><svg width="72" height="72" viewBox="0 0 72 72" fill="none" stroke="#fff" stroke-width="2"><circle cx="36" cy="36" r="30"/><circle cx="36" cy="36" r="24"/><circle cx="36" cy="36" r="6"/><path d="M36 30C30 20 22 16 14 22M42 36c10-6 14-14 8-22M36 42c6 10 14 14 22 8M30 36c-10 6-14 14-8 22"/></svg></div>
    <div class="card-body"><h3 class="card-title">It feels like it belongs to the next generation</h3><p class="card-text">While legacy platforms show their age, Torvik shows what’s next. It looks engineered, not assembled.</p></div>
  </article>

  <article class="abs card" style="left:216px;top:3220px">
    <div class="card-icon"><svg width="72" height="72" viewBox="0 0 72 72" fill="none" stroke="#fff" stroke-width="2"><rect x="6" y="18" width="52" height="36" rx="2"/><path d="M26 54v8M38 54v8M20 62h24M14 30h16M14 38h22M14 46h12"/><circle cx="52" cy="18" r="9"/><circle cx="52" cy="18" r="3"/></svg></div>
    <div class="card-body"><h3 class="card-title">It invites imagination</h3><p class="card-text">Observers can’t help but wonder: What’s inside? What can it do? How is it built so differently?</p></div>
  </article>

  <article class="abs card" style="left:302px;top:3376px">
    <div class="card-icon"><svg width="72" height="72" viewBox="0 0 72 72" fill="none" stroke="#fff" stroke-width="2"><circle cx="36" cy="36" r="28"/><path d="M36 8v56M8 36h56M16 16l40 40M56 16L16 56"/><circle cx="36" cy="36" r="14"/></svg></div>
    <div class="card-body"><h3 class="card-title">It feels like a system, not just an aircraft</h3><p class="card-text">From design to production to deployment, everything about Torvik is intentional — and scalable.</p></div>
  </article>
</section>

<footer class="abs site-footer">
  <div class="brand footer-brand"><span class="brand-dot"></span>TORVIK SKYWORKS</div>
  <nav class="footer-nav">
    <span>Home</span><span class="sep">|</span><span>About Us</span><span class="sep">|</span><span>Why Torvik</span><span class="sep">|</span><span>Investor Info</span><span class="sep">|</span><span>Contact Us</span>
  </nav>
  <div class="contact" style="left:165px">
    <span class="contact-icon"><svg width="16" height="20" viewBox="0 0 16 20"><path d="M8 0a7 7 0 0 0-7 7c0 5 7 13 7 13s7-8 7-13a7 7 0 0 0-7-7z" fill="#050505"/><circle cx="8" cy="7" r="2.6" fill="#fff"/></svg></span>
    <div><h4>Location</h4><p>Torvik Skyworks Inc. 4820 Falconridge Drive<br>Austin, Texas 78730</p></div>
  </div>
  <div class="contact" style="left:550px">
    <span class="contact-icon"><svg width="18" height="18" viewBox="0 0 18 18"><path d="M4 1l3 4-2 2c1 3 3 5 6 6l2-2 4 3-2 3C8 17 1 10 1 3z" fill="#050505"/></svg></span>
    <div><h4>Phone</h4><p>+1 (512) 555 0148</p></div>
  </div>
  <div class="contact" style="left:859px">
    <span class="contact-icon"><svg width="18" height="14" viewBox="0 0 18 14"><rect x="0" y="0" width="18" height="14" rx="2" fill="#050505"/><path d="M1 2l8 6 8-6" fill="none" stroke="#fff" stroke-width="1.5"/></svg></span>
    <div><h4>Email</h4><p>info@torvikskyworks.com</p></div>
  </div>
  <div class="footer-line"></div>
  <div class="social"><span></span><span></span><span></span></div>
  <p class="copyright">Copyright@2025.All Rights Reserved</p>
</footer>

</body>
</html>
```